Elixir labels for new e-liquid line

We will be introducing a new juice line called Tidal Pact and will include three flavors Harbor, Ember and Velvet. We are looking for someone to design the labels for these flavors. Maximum space for the labels will be 4.75 x 2.125 inches (w x h). The height we would like to keep maxed out, the width you can play around with to fit the design. We would like the labels to look like old vintage elixir labels with each flavor having some design element within the main design that separates it apart from the other flavors. Each flavor should look like it part of a whole series. You should see the label and what to pick it up and see what it is. Attached are some sample elixir labels we like.

Requirements
Must have
• Can be in color or Grayscale
• Flavor name and line name
• Nicotine level (three levels for each flavor 0mg, 3mg, and 6mg)
• The following warning: "Do not sell e-juice to anyone under 18. Keep away from children & pets. Do not use if you are pregnant, breastfeeding, diabetic or suffer from high blood-pressure. Nicotine is both addictive and habit-forming. Do not buy if seal is broken. This Product has not yet been regulated by the BQR. Use at your own risk."
• Ingredient list: "Hand crafted in the USA with the highest quality kosher food grade USP Vegetable Glycerin, USP grade propylene, premium nicotine, natural and artificial flavor"

```html
<!DOCTYPE html>
<html lang="en">
<head>
<meta charset="utf-8">
<title>Tidal Pact — Harbor label presentation</title>
<link rel="stylesheet" href="https://fonts.googleapis.com/css2?family=Rye&family=Oswald:wght@500;700&family=Courier+Prime:wght@700&family=Cinzel:wght@700&display=swap">
<style>
  :root {
    --board: #ffffff;
    --frame: #c9c9c9;
    --rule: #e9e9e9;
    --band: #eeeeee;
    --ink: #4a3236;
    --bar: #3b2a2c;
    --paper: #eee8da;
    --paper-dark: #d9cfbb;
    --ornament: #b9aa95;
  }
  * { margin: 0; padding: 0; box-sizing: border-box; }
  html, body { width: 731px; height: 1200px; overflow: hidden; background: var(--board); }
  .board { position: relative; width: 731px; height: 1200px; border: 3px solid var(--frame); background: var(--board); }
  .edge-band { position: absolute; left: 16px; right: 16px; height: 6px; background: var(--rule); }
  .edge-band.top { top: 13px; }
  .edge-band.bottom { bottom: 13px; }
  .divider { position: absolute; left: 16px; right: 16px; top: 470px; height: 2px; background: var(--rule); }

  /* flat label */
  .label { position: absolute; left: 172px; top: 74px; width: 392px; height: 361px;
    background: radial-gradient(ellipse at 50% 45%, var(--paper) 55%, var(--paper-dark) 100%); color: var(--ink); overflow: hidden; }
  .label-bar { position: absolute; left: 0; right: 0; background: var(--bar); }
  .label-bar.top { top: 0; height: 6px; }
  .label-bar.bottom { bottom: 0; height: 8px; }
  .side-panel { position: absolute; top: 6px; bottom: 8px; width: 52px; }
  .side-panel.left { left: 0; border-right: 1px solid var(--ink); }
  .side-panel.right { right: 0; border-left: 1px solid var(--ink); }
  .side-text { position: absolute; left: 50%; top: 50%; width: 330px; font-family: "Courier Prime", monospace;
    font-weight: 700; font-size: 6.3px; line-height: 9px; text-transform: uppercase; letter-spacing: 0.1px;
    transform: translate(-50%, -50%) rotate(-90deg); }
  .label .face { position: absolute; left: 67px; top: 4px; }

  /* shared label face */
  .face { width: 258px; height: 352px; color: var(--ink); }
  .face-frame { position: absolute; inset: 0; }
  .top-ornament { position: absolute; left: 104px; top: 18px; width: 50px; height: 16px; border-radius: 50%;
    background: var(--ornament); opacity: .7; }
  .line-kicker { position: absolute; left: 0; right: 0; top: 56px; text-align: center;
    font-family: "Rye", serif; font-size: 16px; line-height: 20px; letter-spacing: 1px; }
  .line-name { position: absolute; left: 0; right: 0; top: 100px; text-align: center;
    font-family: "Rye", serif; font-weight: 400; font-size: 35px; line-height: 40px; }
  .flourish { position: absolute; left: 32px; top: 168px; width: 194px; height: 50px; border-radius: 24px;
    background: linear-gradient(90deg, var(--ornament), #cdbfa8 50%, var(--ornament)); opacity: .8; }
  .medallion { position: absolute; left: 80px; top: 144px; width: 98px; height: 98px; border-radius: 50%;
    border: 2px solid var(--ink); outline: 1px solid var(--ink); outline-offset: 3px;
    background: radial-gradient(circle, #d9cfbb 0%, #b3a38c 100%); }
  .flavor-box { position: absolute; left: 36px; right: 36px; top: 262px; height: 36px;
    border-top: 2px solid var(--ink); border-bottom: 2px solid var(--ink);
    display: flex; align-items: center; justify-content: center;
    font-family: "Oswald", sans-serif; font-weight: 700; font-size: 22px; letter-spacing: 3px; }
  .flavor-box::before, .flavor-box::after { content: ""; position: absolute; left: 0; right: 0; height: 1px; background: var(--ink); }
  .flavor-box::before { top: 2px; } .flavor-box::after { bottom: 2px; }
  .nicotine { position: absolute; left: 0; right: 0; top: 304px; text-align: center;
    font-family: "Cinzel", serif; font-weight: 700; font-size: 12px; line-height: 16px; letter-spacing: 0.5px; }

  /* variants */
  .variant { position: absolute; top: 603px; width: 110px; text-align: center; }
  .variant.ember { left: 107px; }
  .variant.velvet { left: 512px; }
  .variant-art { width: 108px; height: 108px; border-radius: 50%; margin: 0 auto;
    background: radial-gradient(circle, #efe9e6 0%, #c7b7b9 70%, #7c6366 100%); }
  .variant-name { margin-top: 36px; font-family: "Oswald", sans-serif; font-weight: 700; font-size: 17px;
    letter-spacing: 6px; color: var(--ink); padding-left: 6px; }

  /* bottle */
  .stage-band { position: absolute; left: 16px; right: 16px; top: 899px; height: 143px; background: var(--band); }
  .stage-line { position: absolute; left: 16px; right: 16px; top: 1042px; height: 7px; background: var(--bar); }
  .bottle { position: absolute; left: 0; top: 0; width: 731px; height: 1200px; }
  .bottle-bulb { position: absolute; left: 320px; top: 529px; width: 94px; height: 160px; border-radius: 47px 47px 6px 6px;
    background: linear-gradient(90deg, #111, #3a3a3a 40%, #161616); }
  .bottle-collar { position: absolute; left: 294px; top: 678px; width: 148px; height: 82px; border-radius: 6px;
    background: repeating-linear-gradient(90deg, #141414 0 3px, #2c2c2c 3px 5px); }
  .bottle-body { position: absolute; left: 275px; top: 757px; width: 187px; height: 382px; border-radius: 30px 30px 12px 12px;
    background: linear-gradient(90deg, #4a2208, #9a5419 38%, #7a3c10 70%, #4e2409); }
  .bottle-label { position: absolute; left: 281px; top: 866px; width: 175px; height: 243px; overflow: hidden;
    background: radial-gradient(ellipse at 50% 45%, var(--paper) 55%, var(--paper-dark) 100%); }
  .bottle-label .face { position: absolute; left: 0; top: 0; transform: scale(.678); transform-origin: 0 0; }
</style>
</head>
<body>
<main class="board">
  <div class="edge-band top"></div>

  <section class="label" aria-label="Tidal Pact Harbor label, flat">
    <div class="label-bar top"></div>
    <div class="side-panel left">
      <p class="side-text">This product has not yet been regulated by the BQR. Use at your own risk." Ingredient list: hand crafted in the USA with the highest quality kosher food grade USP vegetable glycerin, USP grade propylene, premium nicotine, natural and artificial flavor.</p>
    </div>

    <div class="face">
      <svg class="face-frame" width="258" height="352" viewBox="0 0 258 352" fill="none" stroke="#4a3236">
        <rect x="1" y="2" width="256" height="346" stroke-width="1.2"/>
        <rect x="5" y="6" width="248" height="338" stroke-width="1"/>
        <rect x="10" y="11" width="238" height="328" stroke-width="1" stroke-dasharray="1.5 2"/>
        <rect x="14" y="15" width="230" height="320" stroke-width="0.8"/>
        <path d="M14 30 H30 V15 M244 30 H228 V15 M14 320 H30 V335 M244 320 H228 V335" stroke-width="1"/>
        <path d="M52 64 Q129 36 206 64" stroke-width="1.2"/>
        <path d="M52 86 Q129 70 206 86" stroke-width="1.2"/>
        <path d="M52 64 L46 75 L52 86 M206 64 L212 75 L206 86" stroke-width="1.2"/>
        <path d="M40 75 l3 -3 l3 3 l-3 3 z M212 75 l3 -3 l3 3 l-3 3 z" fill="#4a3236" stroke="none"/>
        <path d="M36 255 H222 M36 304 H222" stroke-width="0.8" stroke-dasharray="1.5 2"/>
      </svg>
      <div class="top-ornament" role="img" aria-label="Small filigree crest"></div>
      <p class="line-kicker">E-LIQUID</p>
      <h1 class="line-name">TIDAL PACT</h1>
      <div class="flourish" role="img" aria-label="Scrolled flourish framing the medallion"></div>
      <div class="medallion" role="img" aria-label="Engraved sun over hills medallion"></div>
      <p class="flavor-box">HARBOR</p>
      <p class="nicotine">Nicotine Level 3mg</p>
    </div>

    <div class="side-panel right">
      <p class="side-text">Do not sell e-juice to anyone under 18. Keep away from children &amp; pets. Do not use if you are pregnant, breastfeeding, diabetic or suffer from high blood-pressure. Nicotine is both addictive and habit-forming. Do not buy if seal is broken.</p>
    </div>
    <div class="label-bar bottom"></div>
  </section>

  <div class="divider"></div>

  <div class="variant ember">
    <div class="variant-art" role="img" aria-label="Engraved sun emblem for the Ember flavor"></div>
    <p class="variant-name">EMBER</p>
  </div>
  <div class="variant velvet">
    <div class="variant-art" role="img" aria-label="Engraved crescent moon and stars emblem for the Velvet flavor"></div>
    <p class="variant-name">VELVET</p>
  </div>

  <div class="stage-band"></div>
  <div class="stage-line"></div>

  <div class="bottle" aria-label="Amber dropper bottle wearing the Harbor label">
    <div class="bottle-bulb"></div>
    <div class="bottle-collar"></div>
    <div class="bottle-body"></div>
    <div class="bottle-label">
      <div class="face">
        <svg class="face-frame" width="258" height="352" viewBox="0 0 258 352" fill="none" stroke="#4a3236">
          <rect x="1" y="2" width="256" height="346" stroke-width="1.2"/>
          <rect x="5" y="6" width="248" height="338" stroke-width="1"/>
          <rect x="10" y="11" width="238" height="328" stroke-width="1" stroke-dasharray="1.5 2"/>
          <rect x="14" y="15" width="230" height="320" stroke-width="0.8"/>
          <path d="M14 30 H30 V15 M244 30 H228 V15 M14 320 H30 V335 M244 320 H228 V335" stroke-width="1"/>
          <path d="M52 64 Q129 36 206 64" stroke-width="1.2"/>
          <path d="M52 86 Q129 70 206 86" stroke-width="1.2"/>
          <path d="M52 64 L46 75 L52 86 M206 64 L212 75 L206 86" stroke-width="1.2"/>
          <path d="M40 75 l3 -3 l3 3 l-3 3 z M212 75 l3 -3 l3 3 l-3 3 z" fill="#4a3236" stroke="none"/>
          <path d="M36 255 H222 M36 304 H222" stroke-width="0.8" stroke-dasharray="1.5 2"/>
        </svg>
        <div class="top-ornament" role="img" aria-label="Small filigree crest"></div>
        <p class="line-kicker">E-LIQUID</p>
        <p class="line-name">TIDAL PACT</p>
        <div class="flourish" role="img" aria-label="Scrolled flourish framing the medallion"></div>
        <div class="medallion" role="img" aria-label="Engraved sun over hills medallion"></div>
        <p class="flavor-box">HARBOR</p>
        <p class="nicotine">Nicotine Level 3mg</p>
      </div>
    </div>
  </div>

  <div class="edge-band bottom"></div>
</main>
</body>
</html>
```